Esthetically Pleasing Core Values and Brand Promise for Accounting Firm

I would like a cohesive design that ties together my core values and brand promise. My firm, Maple Finch Advisory, provides accounting work to small businesses. I prefer modern and clean designs. I want my Core Values and Brand Promise to represent me - sole entrepreneur, married, mother of two kids, modern esthetics, clean lines, organized, colorful (teals, greys, white, yellows)

Industry/Entity Type

Public Accounting

Colors
33b8a4

```html
<!DOCTYPE html>
<html lang="en">
<head>
<meta charset="utf-8">
<title>Maple Finch Advisory – Core Values</title>
<link rel="stylesheet" href="https://fonts.googleapis.com/css2?family=Montserrat:wght@400;600;700&family=Barlow+Condensed:wght@500&display=swap">
<style>
  :root {
    --teal: #33b8a4;
    --teal-bright: #17b295;
    --teal-mid: #1a9a90;
    --teal-deep: #0f5b57;
    --ink: #2b2b2b;
    --white: #ffffff;
    --photo-light: #e9eef2;
    --photo-blue: #b9d3e6;
  }
  * { margin: 0; padding: 0; box-sizing: border-box; }
  html, body { width: 889px; height: 1200px; overflow: hidden; background: var(--white); }
  .flyer { position: relative; width: 889px; height: 1200px; overflow: hidden; background: var(--white); font-family: "Barlow Condensed", sans-serif; }

  .hero-photo {
    position: absolute; left: 0; top: 0; width: 889px; height: 640px;
    background: linear-gradient(160deg, var(--photo-light) 0%, #dfe6ea 30%, var(--photo-blue) 55%, #d5dfe6 75%, #c9cfd3 100%);
  }
  .waves { position: absolute; left: 0; top: 0; width: 889px; height: 1200px; }

  .brand-tab {
    position: absolute; left: 46px; top: 0; width: 246px; height: 272px;
    background: rgba(255,255,255,0.94);
    border-radius: 0 0 123px 123px;
    display: flex; flex-direction: column; align-items: center; justify-content: center;
    padding-bottom: 30px;
  }
  .brand-name {
    font-family: "Montserrat", sans-serif; font-weight: 400; color: var(--teal-mid);
    text-align: center; font-size: 30px; line-height: 1.2; letter-spacing: 2px; text-transform: uppercase;
  }

  .section-title {
    position: absolute; left: 49px; top: 355px;
    font-family: "Montserrat", sans-serif; font-weight: 700; color: var(--white);
    font-size: 49px; line-height: 52px;
  }

  .value-card {
    position: absolute; top: 535px; width: 176px; height: 356px;
    border-radius: 88px;
    background: linear-gradient(90deg, var(--teal-deep) 0%, var(--teal-mid) 100%);
    box-shadow: 0 0 0 4px var(--white);
    color: var(--white); text-align: center;
  }
  .value-card .icon { position: absolute; left: 34px; top: 18px; width: 108px; height: 108px; }
  .value-card .label {
    position: absolute; left: 8px; right: 8px; top: 141px; height: 40px;
    border-top: 1.5px solid var(--white); border-bottom: 1.5px solid var(--white);
    font-family: "Montserrat", sans-serif; font-weight: 600; font-size: 18px; line-height: 37px;
  }
  .value-card .text { position: absolute; left: 12px; right: 12px; top: 199px; font-size: 18px; line-height: 23.5px; }

  .brand-promise {
    position: absolute; left: 60px; top: 931px; width: 768px; height: 53px;
    border: 1.5px solid var(--ink);
    font-family: "Montserrat", sans-serif; font-weight: 700; font-size: 18.5px; color: var(--ink);
    display: flex; align-items: center; justify-content: center; letter-spacing: 0.2px;
  }

  .service { position: absolute; top: 1004px; color: var(--ink); }
  .service h2 { font-family: "Montserrat", sans-serif; font-weight: 600; font-size: 29px; line-height: 36px; }
  .service p { font-size: 19px; line-height: 23.5px; margin-top: 4px; }
  .service-tax { right: 404px; text-align: right; width: 440px; }
  .service-accounting { left: 516px; text-align: left; width: 330px; }

  .footer-band { position: absolute; left: 0; bottom: 0; width: 889px; height: 21px; background: var(--teal-mid); }
</style>
</head>
<body>
<main class="flyer">
  <div class="hero-photo" role="img" aria-label="Photo of an accountant in a light blue shirt working at a desk with a calculator and printed charts"></div>

  <svg class="waves" viewBox="0 0 889 1200" aria-hidden="true">
    <defs>
      <linearGradient id="waveTeal" x1="0" y1="0" x2="1" y2="1">
        <stop offset="0" stop-color="#17b295"/>
        <stop offset="1" stop-color="#168c86"/>
      </linearGradient>
    </defs>
    <path d="M0,225 C140,170 300,250 390,380 C455,480 530,590 650,580 C745,572 820,520 889,430 L889,700 L0,700 Z" fill="#2a8f8a"/>
    <path d="M0,245 C140,195 290,270 375,395 C440,495 520,600 640,595 C740,590 815,540 889,455 L889,700 L0,700 Z" fill="url(#waveTeal)"/>
    <path d="M0,600 C110,535 250,515 390,545 C500,570 580,605 680,595 C780,585 840,555 889,525 L889,1200 L0,1200 Z" fill="#ffffff"/>
    <path d="M0,600 C110,535 250,515 390,545 C500,570 580,605 680,595 C780,585 840,555 889,525" fill="none" stroke="#17b295" stroke-width="6"/>
  </svg>

  <div class="brand-tab">
    <div class="brand-name">Maple Finch<br>Advisory</div>
  </div>

  <h1 class="section-title">Core<br>Values</h1>

  <section class="value-card" style="left:48px">
    <svg class="icon" viewBox="0 0 108 108" fill="none" stroke="#fff" stroke-width="2" stroke-linecap="round" stroke-linejoin="round" aria-hidden="true">
      <circle cx="54" cy="54" r="52"/>
      <path d="M40 48 v-6 a4 4 0 0 1 8 0 v-2 a4 4 0 0 1 8 0 v1 a4 4 0 0 1 8 0 v3 a4 4 0 0 1 6 3 v10 c0 8 -4 12 -6 14 v8 h-20 v-8 c-3 -3 -5 -6 -5 -10 z"/>
      <path d="M54 22 v6 M42 26 l3 5 M66 26 l-3 5 M34 34 l5 3 M74 34 l-5 3"/>
    </svg>
    <div class="label">Empower</div>
    <p class="text">we are dedicated, appreciative and respectful of people’s time and purpose.</p>
  </section>

  <section class="value-card" style="left:254px">
    <svg class="icon" viewBox="0 0 108 108" fill="none" stroke="#fff" stroke-width="2" stroke-linecap="round" aria-hidden="true">
      <circle cx="54" cy="54" r="52"/>
      <circle cx="54" cy="54" r="26"/>
      <path d="M54 20 v14 M54 74 v14 M20 54 h14 M74 54 h14"/>
      <circle cx="54" cy="48" r="6"/>
      <path d="M42 66 c0-7 5-11 12-11 s12 4 12 11 z"/>
    </svg>
    <div class="label">Client Focused</div>
    <p class="text">we provide a personal service that goes above the standards of professional care.</p>
  </section>

  <section class="value-card" style="left:459px">
    <svg class="icon" viewBox="0 0 108 108" fill="none" stroke="#fff" stroke-width="2" stroke-linecap="round" stroke-linejoin="round" aria-hidden="true">
      <circle cx="54" cy="54" r="52"/>
      <path d="M54 24 v50 M30 34 h48 M42 78 h24 M46 74 h16"/>
      <circle cx="54" cy="24" r="3"/>
      <path d="M30 34 l-10 22 h20 z M78 34 l-10 22 h20 z"/>
    </svg>
    <div class="label">Rectitude</div>
    <p class="text">we know the difference between what we have the right to do and what the right thing to do is.</p>
  </section>

  <section class="value-card" style="left:664px">
    <svg class="icon" viewBox="0 0 108 108" fill="none" aria-hidden="true">
      <circle cx="54" cy="54" r="52" stroke="#fff" stroke-width="2"/>
      <path d="M60 26 L42 58 H54 L49 84 L68 48 H56 Z" fill="#fff"/>
    </svg>
    <div class="label">Relentless</div>
    <p class="text">we believe that the longer we try to do our best, the better we become.</p>
  </section>

  <div class="brand-promise">BRAND PROMISE – TRUST, TRANSPARENCY AND DEPENDABILITY</div>

  <section class="service service-tax">
    <h2>TAX:</h2>
    <p>Maple Finch provides all clients with a trusted tax advisor<br>who provides accuracy in all filings and ensures<br>your compliance with all government agencies.</p>
  </section>

  <section class="service service-accounting">
    <h2>ACCOUNTING:</h2>
    <p>Maple Finch provides all business owners<br>with the financial visibility needed to<br>foster growth and facilitate goals.</p>
  </section>

  <div class="footer-band"></div>
</main>
</body>
</html>
```